Equestrian brand 'health check' webinar template

I am looking to host a series of webinars promoting my consulting business in equestrian business development. I work mainly with start-ups and young brands looking to establish their brand in the international equestrian marketplace mainly focussed on horse riding fashion and horse riding essentials.
The topic of the webinar is a 'brand health check': helping brands understand what they really stand for if they are really 'talking' to the right audience and delivering the right message. Additionally, we'll touch on having all the brand fundamentals in place to become successful.
I am looking for a webinar/presentation template that is professional and shows off the topics in the best possible way, in keeping with the equestrian theme and the current look and feel of the website: brightmeadowadvisory.example
Target Market(s)
Equestrian businesses, start-up, fashion
Industry/Entity Type
Business
Logo Text
conceptual high market equestrian services style
Colors
Designer to choose colors to be used in the design.

```html
<!DOCTYPE html>
<html lang="en">
<head>
<meta charset="utf-8">
<title>Brand Health Check – Webinar Template</title>
<link rel="stylesheet" href="https://fonts.googleapis.com/css2?family=Raleway:wght@400;600;800&family=Roboto+Slab:wght@300;400&display=swap">
<style>
  :root {
    --bg: #dfe0e2;
    --mauve: #b996b8;
    --plum: #7a4a7a;
    --lilac: #d3b6d3;
    --ink: #222;
    --white: #fff;
    --host-red: #a53a3f;
    --photo-dark: linear-gradient(160deg, #3d4440 0%, #2a302e 45%, #4a4d4b 100%);
  }
  * { box-sizing: border-box; margin: 0; padding: 0; }
  html, body { width: 1200px; height: 1200px; overflow: hidden; background: var(--bg); }
  body { position: relative; font-family: "Roboto Slab", serif; font-weight: 300; color: var(--white); }
  .slide { position: absolute; width: 531px; height: 299px; overflow: hidden; box-shadow: 0 3px 6px rgba(0,0,0,.18); }
  .col-left { left: 55px; } .col-right { left: 627px; }
  .row-1 { top: 82px; } .row-2 { top: 450px; } .row-3 { top: 819px; }
  .abs { position: absolute; }
  .photo { position: absolute; inset: 0; }
  .photo--stable { background: var(--photo-dark); }
  .photo--boot { background: linear-gradient(150deg, #5a5a5a 0%, #2b2b2b 55%, #444 100%); }
  .photo--race { background: linear-gradient(180deg, #b9c9d8 0%, #6d8a5c 40%, #4d6a3a 70%, #7aa04e 100%); }
  .heading { font-family: "Raleway", sans-serif; font-weight: 800; text-transform: uppercase; line-height: 1; }
  .brand { display: flex; align-items: center; gap: 8px; font-family: "Roboto Slab", serif; font-weight: 400; text-transform: uppercase; line-height: 1.05; }
  .brand-dot { border-radius: 50%; flex: none; }
  .brand--light { color: var(--white); } .brand--light .brand-dot { background: var(--white); }
  .brand--mauve { color: var(--mauve); } .brand--mauve .brand-dot { background: var(--mauve); }

  .pill { background: var(--mauve); border-radius: 12px; color: var(--white); font-family: "Raleway", sans-serif; font-weight: 400; letter-spacing: 2px; font-size: 11px; display: flex; align-items: center; justify-content: center; }
  .meta { display: flex; align-items: center; gap: 7px; font-size: 11.5px; font-weight: 400; }
  .meta-icon { width: 20px; height: 20px; border-radius: 50%; background: var(--mauve); display: flex; align-items: center; justify-content: center; }
  .cta { background: var(--mauve); border-radius: 15px; font-size: 13px; font-weight: 400; display: flex; align-items: center; justify-content: center; text-transform: uppercase; }

  .band { position: absolute; left: 0; right: 0; background: var(--mauve); }
  .panel-mauve { background: var(--mauve); }
  .silhouette { position: absolute; background: radial-gradient(ellipse at 55% 60%, var(--lilac) 0%, rgba(211,182,211,.55) 45%, rgba(211,182,211,0) 72%); }

  .avatar { border-radius: 50%; background: var(--white); border: 5px solid #7c6370; }
  .host-badge { border-radius: 50%; background: var(--host-red); font-family: "Raleway", sans-serif; font-size: 11px; font-weight: 400; display: flex; align-items: center; justify-content: center; }
  .contact { display: flex; align-items: center; gap: 9px; font-size: 9px; }
  .contact svg { flex: none; }

  .topic { position: absolute; width: 140px; height: 140px; border-radius: 50%; background: var(--plum); text-align: center; padding-top: 37px; }
  .topic h3 { font-family: "Raleway", sans-serif; font-weight: 600; font-size: 13.5px; margin-bottom: 5px; }
  .topic p { font-size: 7.8px; line-height: 1.5; padding: 0 22px; color: #efe3ef; }

  .content-list { list-style: none; font-size: 7.8px; color: var(--ink); }
  .content-list li { height: 23.6px; }
  .content-list li::before { content: "· "; color: var(--mauve); }
</style>
</head>
<body>

<!-- Webinar cover -->
<section class="slide col-left row-1">
  <div class="photo photo--stable" role="img" aria-label="Photo of a grey horse walking past a wooden stable on a sand arena, darkened"></div>
  <div class="brand brand--light abs" style="left:26px;top:31px;font-size:15px;">
    <span class="brand-dot" style="width:58px;height:58px;"></span>
    <span>Bright Meadow<br>Advisory</span>
  </div>
  <div class="pill abs" style="left:27px;top:131px;width:91px;height:21px;">WEBINAR</div>
  <h1 class="heading abs" style="left:27px;top:168px;font-size:28px;">Brand Health Check</h1>
  <p class="abs" style="left:27px;top:199px;width:335px;font-size:7.8px;line-height:1.5;">Helping brands understand what they really stand for if they are really ‘talking’ to the right audience and delivering the right message. Additionally, we’ll touch on having all the brand fundamentals in place to become successful.</p>
  <div class="meta abs" style="left:29px;top:255px;">
    <span class="meta-icon"><svg width="10" height="10" viewBox="0 0 10 10"><rect x="1" y="2" width="8" height="7" fill="none" stroke="#fff" stroke-width="1.2"/><line x1="1" y1="4.3" x2="9" y2="4.3" stroke="#fff"/></svg></span>
    Wednesday, 14 March 2018
  </div>
  <div class="meta abs" style="left:227px;top:255px;">
    <span class="meta-icon"><svg width="10" height="10" viewBox="0 0 10 10"><circle cx="5" cy="5" r="4" fill="none" stroke="#fff" stroke-width="1.2"/><path d="M5 2.6V5h2" fill="none" stroke="#fff"/></svg></span>
    19:00 (GMT -7)
  </div>
  <div class="cta abs" style="left:365px;top:250px;width:136px;height:30px;">Register Now</div>
</section>

<!-- Webinar title -->
<section class="slide col-right row-1">
  <div class="photo photo--stable" role="img" aria-label="Photo of a grey horse walking past a wooden stable on a sand arena, darkened"></div>
  <div class="brand brand--light abs" style="left:26px;top:31px;font-size:15px;">
    <span class="brand-dot" style="width:58px;height:58px;"></span>
    <span>Bright Meadow<br>Advisory</span>
  </div>
  <div class="band" style="top:143px;height:72px;"></div>
  <p class="abs" style="left:27px;top:158px;font-family:'Raleway',sans-serif;font-weight:400;font-size:13px;">WEBINAR</p>
  <h1 class="heading abs" style="left:27px;top:177px;font-size:28px;">Brand Health Check</h1>
  <p class="abs" style="left:29px;top:253px;font-size:11.5px;font-weight:400;">www.brightmeadowadvisory.example</p>
</section>

<!-- Host -->
<section class="slide col-left row-2 panel-mauve">
  <div class="silhouette" style="left:297px;top:180px;width:234px;height:119px;" role="img" aria-label="Faint galloping horse silhouette"></div>
  <div class="avatar abs" style="left:100px;top:74px;width:106px;height:106px;"></div>
  <div class="host-badge abs" style="left:91px;top:79px;width:37px;height:37px;">Host</div>
  <p class="abs" style="left:60px;width:185px;text-align:center;top:191px;font-family:'Raleway',sans-serif;font-weight:600;font-size:18px;">Jordan Reyes</p>
  <p class="abs" style="left:60px;width:185px;text-align:center;top:214px;font-size:11px;">Director</p>
  <div class="abs" style="left:252px;top:67px;width:1px;height:173px;background:#f1e5f1;"></div>
  <p class="abs" style="left:288px;top:82px;width:200px;font-size:8.8px;line-height:1.35;">Lorem ipsum dolor sit amet, consectetuer adipiscing elit, sed diam nonummy nibh euismod tincidunt ut laoreet dolore</p>
  <div class="contact abs" style="left:290px;top:137px;">
    <svg width="14" height="10" viewBox="0 0 14 10"><rect width="14" height="10" fill="var(--host-red)"/><path d="M0 0l7 5.5L14 0" fill="none" stroke="#b996b8" stroke-width="1.2"/></svg>
    jordan@brightmeadowadvisory.example
  </div>
  <div class="contact abs" style="left:290px;top:169px;">
    <svg width="14" height="12" viewBox="0 0 24 24"><path fill="var(--host-red)" d="M6.6 10.8a15.1 15.1 0 0 0 6.6 6.6l2.2-2.2c.3-.3.7-.4 1-.2 1.1.4 2.3.6 3.6.6.6 0 1 .4 1 1V20c0 .6-.4 1-1 1A17 17 0 0 1 3 4c0-.6.4-1 1-1h3.5c.6 0 1 .4 1 1 0 1.3.2 2.5.6 3.6.1.3 0 .7-.2 1z"/></svg>
    555-010-0199
  </div>
  <div class="contact abs" style="left:290px;top:205px;">
    <svg width="14" height="12" viewBox="0 0 14 12"><circle cx="7" cy="6" r="5.5" fill="var(--host-red)"/></svg>
    JordanReyes
  </div>
</section>

<!-- Topics -->
<section class="slide col-right row-2 panel-mauve">
  <h2 class="heading abs" style="left:28px;top:35px;font-weight:600;font-size:22px;">Lorem Ipsum Sit Amet</h2>
  <div class="topic" style="left:21px;top:76px;"><h3>PERSONAL</h3><p>Lorem ipsum dolor sit amet, consectetuer Lorem ipsum dolor sit amet, consectetuer adipiscing elit, sed diam nonummy.</p></div>
  <div class="topic" style="left:195px;top:76px;"><h3>PROFESSIONAL</h3><p>Lorem ipsum dolor sit amet, consectetuer Lorem ipsum dolor sit amet, consectetuer adipiscing elit.</p></div>
  <div class="topic" style="left:370px;top:76px;"><h3>PERFORMANCE</h3><p>Lorem ipsum dolor sit amet, consectetuer Lorem ipsum dolor sit amet, consectetuer adipiscing elit, sed diam nonummy.</p></div>
  <div class="abs" style="left:0;right:0;top:244px;bottom:0;background:var(--white);"></div>
  <div class="silhouette" style="left:17px;top:210px;width:208px;height:89px;" role="img" aria-label="Galloping horse silhouette"></div>
  <div class="brand brand--mauve abs" style="left:394px;top:258px;font-size:10px;gap:5px;">
    <span class="brand-dot" style="width:30px;height:30px;"></span>
    <span>Bright Meadow<br>Advisory</span>
  </div>
</section>

<!-- Session divider -->
<section class="slide col-left row-3">
  <div class="photo photo--boot" role="img" aria-label="Black and white close-up of a rider's boot in a stirrup against a dark horse"></div>
  <div class="abs" style="left:0;top:119px;width:20px;height:54px;background:var(--mauve);"></div>
  <p class="abs" style="left:29px;top:121px;font-family:'Raleway',sans-serif;font-weight:400;font-size:13px;">SESSION 1</p>
  <h2 class="heading abs" style="left:29px;top:137px;font-size:39px;font-weight:800;">Title Session 1</h2>
  <div class="brand brand--light abs" style="left:33px;top:238px;font-size:11px;gap:6px;">
    <span class="brand-dot" style="width:37px;height:37px;"></span>
    <span>Bright Meadow<br>Advisory</span>
  </div>
</section>

<!-- Session content -->
<section class="slide col-right row-3" style="background:var(--white);">
  <h2 class="heading abs" style="left:27px;top:28px;font-size:23px;font-weight:800;color:var(--mauve);">Title Session 1</h2>
  <p class="abs" style="left:27px;top:65px;width:222px;font-size:7.8px;line-height:1.5;color:var(--ink);">Lorem ipsum dolor sit amet, consectetuer adipiscing elit, sed diam nonummy nibh euismod tincidunt ut laoreet dolore magna aliquam erat volutpat.Ut wisi enim ad minim veniam, quis nostrud exerci tation ullamcorper suscipit lobortis nisl:</p>
  <ul class="content-list abs" style="left:27px;top:137px;">
    <li>Lorem ipsum dolor sit amet 1</li>
    <li>Lorem ipsum dolor sit amet 2</li>
    <li>Lorem ipsum dolor sit amet 3</li>
    <li>Lorem ipsum dolor sit amet 4</li>
    <li>Lorem ipsum dolor sit amet 5</li>
  </ul>
  <div class="abs photo--race" style="left:275px;top:0;right:0;bottom:0;" role="img" aria-label="Photo of jockeys racing horses on a grass track below green hills"></div>
</section>

</body>
</html>
```